Stationary, letterhead, envelopes, 5 x 7 sales card, slide template

1. 5 x 7 sales handout card that can be populated with variable text by our staff and then sent for printing. The back of this card can be the same as the back of the business card you already designed.

2. Company stationary, letterhead and envelope.

3. A fillable slide that can be used in Microsoft Publisher or similar program so we may use it as slides on presentations or for printing. 8.5" x 11" both portrait and landscape forms

This is a private design. already working with a designer

```html
<!DOCTYPE html>
<html lang="en">
<head>
<meta charset="utf-8">
<title>VentoLink – Sales Card</title>
<link rel="stylesheet" href="https://fonts.googleapis.com/css2?family=Questrial&display=swap">
<style>
  :root {
    --stage: #1c1c1c;
    --brand-purple: #8b2673;
    --mark-grey: #c9c9c9;
    --mark-grey-dark: #a9a9a9;
    --paper: #ffffff;
    --url-grey: #d6d6d6;
  }
  * { margin: 0; padding: 0; box-sizing: border-box; }
  html, body {
    width: 1200px; height: 1200px; overflow: hidden;
    background: var(--stage);
    font-family: "Questrial", "Century Gothic", sans-serif;
  }
  .card {
    position: absolute;
    width: 770px; height: 585px;
  }
  .card--back { left: 380px; top: 15px; background: var(--brand-purple); }
  .card--front { left: 64px; top: 590px; background: var(--paper); }

  .brand { position: absolute; }
  .brand__row { display: flex; align-items: center; gap: 14px; }
  .brand__name { font-size: 48px; line-height: 1; letter-spacing: 0.5px; }
  .brand__dot { width: 30px; height: 30px; border-radius: 50%; }
  .brand__tagline {
    font-size: 14px; letter-spacing: 1.2px; margin-top: 6px; padding-left: 2px;
  }

  .card--back .brand { left: 222px; top: 425px; }
  .card--back .brand__name,
  .card--back .brand__tagline { color: var(--mark-grey); }
  .card--back .brand__dot { background: var(--mark-grey); }

  .card--front .brand { left: 236px; top: 48px; }
  .card--front .brand__name { color: var(--mark-grey-dark); }
  .card--front .brand__tagline { color: var(--brand-purple); }
  .card--front .brand__dot { background: var(--mark-grey-dark); }

  .web {
    position: absolute; left: 212px; top: 522px;
    display: flex; align-items: center; gap: 12px;
    color: var(--url-grey); font-size: 15px; letter-spacing: 1px;
  }
  .web__rule { width: 55px; height: 1px; background: var(--url-grey); }
</style>
</head>
<body>
  <section class="card card--back" aria-label="Card back">
    <div class="brand">
      <div class="brand__row">
        <span class="brand__name">VentoLink</span>
        <span class="brand__dot"></span>
      </div>
      <div class="brand__tagline">ALWAYS ON, ALWAYS UP</div>
    </div>
    <div class="web">
      <span class="web__rule"></span>
      <span class="web__url">www.ventolink.com</span>
      <span class="web__rule"></span>
    </div>
  </section>

  <section class="card card--front" aria-label="Card front">
    <div class="brand">
      <div class="brand__row">
        <span class="brand__name">VentoLink</span>
        <span class="brand__dot"></span>
      </div>
      <div class="brand__tagline">ALWAYS ON, ALWAYS UP</div>
    </div>
  </section>
</body>
</html>
```